Clearvane glass & hardware manufacturer

Need a SEO friendly, modern & professional looking website. We are selling all kinds of glass & accessories ( Glass/ Mirror/ splash back/ pool fence/ balustrade/ hardware...we are specialised on some special glass, like curve glass,tinted glass thermal & accoustic glass...) It should has simple & crisp feeling like a glass. It must be fully functional with product display and online ordering. Please see attached confirmed logo design(Blue & white). Make sure the theme color match its feel.

Target Market(s)

Architect and designer, Builder, & Developer

Industry/Entity Type

Manufacturer

Coding

Coded - Design and coding required

Font styles to use
Serif
Sans Serif

Colors

Designer to choose colors to be used in the design.

Requirements
Must have
• Glass & hardware theme and our logo
• Here are some competitor's website for reference. (Borrow ideas but not copy : )
• 1.https://www.lumaro.com.au/about
• 2.http://www.brightpanedirect.com.au/
• 3.http://www.tvk.com.au/
• 4.http://www.oakridgefittings.com.au/
Nice to have
• Some transparent or semi transparent effects to make the website like a glass
Should not have
• No limitation for your imagination

```html
<!DOCTYPE html>
<html lang="en">
<head>
<meta charset="utf-8">
<title>Clearvane Glass &amp; Hardware</title>
<link href="https://fonts.googleapis.com/css2?family=Questrial&family=Open+Sans:wght@400;600&display=swap" rel="stylesheet">
<style>
:root{
  --blue:#2a9fd8;
  --blue-light:#3bb4e8;
  --ink:#3a3a3a;
  --text:#555;
  --page:#ffffff;
  --header:#f3f4f5;
  --section:#ebecee;
  --footer:#333333;
  --footer-text:#bdbdbd;
  --white:#ffffff;
}
*{margin:0;padding:0;box-sizing:border-box}
html,body{width:806px;height:1200px;overflow:hidden}
body{position:relative;background:var(--page);font-family:'Open Sans',sans-serif;color:var(--text)}
.abs{position:absolute}
.site-header{left:0;top:0;width:806px;height:80px;background:linear-gradient(100deg,var(--header) 0%,#fafafa 60%,var(--header) 100%)}
.brand{left:89px;top:18px;display:flex;align-items:center;gap:8px}
.brand-mark{width:40px;height:40px;background:var(--blue)}
.brand-name{font-family:'Questrial',sans-serif;font-size:22px;color:var(--blue);line-height:1}
.brand-sub{font-family:'Questrial',sans-serif;font-size:9.5px;letter-spacing:3px;color:var(--ink);margin-top:3px}
.quote-btn{left:635px;top:17px;width:82px;height:27px;background:var(--blue);color:var(--white);font-family:'Questrial',sans-serif;font-size:10.5px;display:flex;align-items:center;justify-content:center;box-shadow:2px 2px 0 #1b7fb0}
.main-nav{right:89px;top:56px;display:flex;gap:21px;font-family:'Questrial',sans-serif;font-size:10px;color:var(--ink)}
.main-nav .active{color:var(--blue)}
.hero{left:0;top:80px;width:806px;height:332px;background:linear-gradient(100deg,#8f9aa4 0%,#c4ccd2 30%,#e8eaec 55%,#d7dde2 75%,#7e94a8 100%)}
.hero-title{right:89px;top:146px;text-align:right;font-family:'Questrial',sans-serif;font-size:26px;line-height:28px;color:#7d7d7d}
.hero-arrow{top:236px;width:17px;height:21px;background:#3c3c3c;display:flex;align-items:center;justify-content:center}
.welcome-title{left:0;width:806px;top:460px;text-align:center;font-family:'Questrial',sans-serif;font-size:21px;color:var(--blue)}
.welcome-text{left:92px;width:622px;top:494px;text-align:center;font-size:8.6px;line-height:16px;color:var(--text)}
.products{left:0;top:593px;width:806px;height:429px;background:linear-gradient(160deg,var(--section) 0%,#f2f3f4 40%,var(--section) 100%)}
.products-title{left:0;width:806px;top:48px;text-align:center;font-family:'Questrial',sans-serif;font-size:21px;color:var(--blue)}
.tile{width:113px;height:134px;box-shadow:2px 2px 3px rgba(0,0,0,.18);background:var(--white)}
.tile-photo{width:113px;height:102px}
.tile-label{height:32px;background:linear-gradient(var(--blue-light),var(--blue));color:var(--white);font-family:'Questrial',sans-serif;font-size:8.5px;line-height:10px;display:flex;align-items:center;justify-content:center;text-align:center;padding:0 6px}
.site-footer{left:0;top:1022px;width:806px;height:178px;background:var(--footer);color:var(--footer-text)}
.footer-heading{font-size:10px;font-weight:600;color:var(--white)}
.footer-list{list-style:none;font-size:6.8px;line-height:15px;margin-top:8px}
.footer-list li::before{content:"• "}
.social li{display:flex;align-items:center;gap:7px;line-height:20px}
.social li::before{content:none}
.social .dot{width:6px;height:6px;border-radius:50%;background:var(--footer-text)}
.newsletter{left:556px;top:1072px;width:162px;height:27px;background:var(--white);display:flex;align-items:center;justify-content:space-between;padding:0 10px;font-size:7px;color:#444}
.footer-rule{left:89px;top:1155px;width:628px;height:1px;background:#5a5a5a}
.copyright{left:0;width:806px;top:1173px;text-align:center;font-size:7px;color:var(--footer-text)}
</style>
</head>
<body>
<header class="site-header abs">
  <div class="brand abs">
    <span class="brand-mark"></span>
    <div><div class="brand-name">CLEARVANE</div><div class="brand-sub">GLASS &amp; HARDWARE</div></div>
  </div>
  <a class="quote-btn abs">GET A QUOTE</a>
  <nav class="main-nav abs">
    <span class="active">HOME</span><span>ABOUT US</span><span>OUR PRODUCTS</span><span>DIY</span><span>CONTACT</span>
  </nav>
</header>

<section class="hero abs" role="img" aria-label="Glass facade of a modern office tower overlooking a city skyline"></section>
<h1 class="hero-title abs">ETIAM MATTIS<br>AUGUE VEHICULA</h1>
<a class="hero-arrow abs" style="left:0"><svg width="8" height="12" viewBox="0 0 8 12"><path d="M7 1L2 6l5 5" stroke="#fff" fill="none" stroke-width="1.2"/></svg></a>
<a class="hero-arrow abs" style="right:0"><svg width="8" height="12" viewBox="0 0 8 12"><path d="M1 1l5 5-5 5" stroke="#fff" fill="none" stroke-width="1.2"/></svg></a>

<h2 class="welcome-title abs">WELCOME TO CLEARVANE GLASS &amp; HARDWARES</h2>
<p class="welcome-text abs">Proin a dolor mauris. Vestibulum ante ipsum primis in faucibus orci luctus et ultrices posuere cubilia Curae; Vestibulum eget nisl metus. Phasellus nisl est, condimentum vitae faucibus in, sollicitudin vel metus. Nunc sit amet consequat risus. Curabitur ac elit leo. In eleifend dui tellus, in scelerisque elit porttitor et. Integer eu massa lacinia, lacinia nulla non, volutpat purus. Sed libero felis, vestibulum et dolor eget, lacinia aliquet neque.</p>

<section class="products abs">
  <h2 class="products-title abs">OUR PRODUCTS</h2>
  <div class="tile abs" style="left:89px;top:84px"><div class="tile-photo" role="img" aria-label="Glass door with steel pull handles" style="background:linear-gradient(#b9c3c9,#8d979e)"></div><div class="tile-label">GLASS</div></div>
  <div class="tile abs" style="left:217px;top:84px"><div class="tile-photo" role="img" aria-label="Bathroom vanity with wall mirror" style="background:linear-gradient(#c9ced2,#a9b0b6)"></div><div class="tile-label">MIRROR</div></div>
  <div class="tile abs" style="left:345px;top:84px"><div class="tile-photo" role="img" aria-label="Kitchen with glass splash back" style="background:linear-gradient(#e6e2dc,#b08a64)"></div><div class="tile-label">SPLASH BACK</div></div>
  <div class="tile abs" style="left:473px;top:84px"><div class="tile-photo" role="img" aria-label="Rooftop pool with glass fence" style="background:linear-gradient(#6aa3d6,#3fb4d8)"></div><div class="tile-label">POOL FENCE</div></div>
  <div class="tile abs" style="left:601px;top:84px"><div class="tile-photo" role="img" aria-label="Timber staircase with glass balustrade" style="background:linear-gradient(#dfe4e6,#d4aa66)"></div><div class="tile-label">BALUSTRADE</div></div>
  <div class="tile abs" style="left:89px;top:234px"><div class="tile-photo" role="img" aria-label="Chrome glass hinge fitting" style="background:linear-gradient(#ebe8df,#c9c1ac)"></div><div class="tile-label">HARDWARE</div></div>
  <div class="tile abs" style="left:217px;top:234px"><div class="tile-photo" role="img" aria-label="Glass partitioned meeting room" style="background:linear-gradient(#c4cbce,#98a2a6)"></div><div class="tile-label">SPECIAL WORK<br>GLASS</div></div>
  <div class="tile abs" style="left:345px;top:234px"><div class="tile-photo" role="img" aria-label="Curved glass atrium roof" style="background:linear-gradient(#d5dce1,#9fadb8)"></div><div class="tile-label">CURVE GLASS</div></div>
  <div class="tile abs" style="left:473px;top:234px"><div class="tile-photo" role="img" aria-label="Blue tinted glass building facade" style="background:linear-gradient(#2f6aa6,#6fb0e0)"></div><div class="tile-label">TINTED GLASS</div></div>
  <div class="tile abs" style="left:601px;top:234px"><div class="tile-photo" role="img" aria-label="Workers installing wall insulation" style="background:linear-gradient(#d9cfbd,#b5a68b)"></div><div class="tile-label">THERMAL &amp; ACOUSTIC<br>GLASS</div></div>
</section>

<footer class="site-footer abs">
  <div class="abs" style="left:89px;top:26px"><div class="footer-heading">Links</div>
    <ul class="footer-list"><li>Home</li><li>About Us</li><li>Our Products</li><li>DIY Contact</li></ul></div>
  <div class="abs" style="left:180px;top:26px"><div class="footer-heading">Products</div>
    <ul class="footer-list"><li>Glass</li><li>Mirror</li><li>Splash back</li><li>Pool fence</li></ul></div>
  <ul class="footer-list abs" style="left:244px;top:37px"><li>Balustrade</li><li>Hardware</li><li>Special work glass</li><li>Curve glass</li></ul>
  <ul class="footer-list abs" style="left:324px;top:37px"><li>Tinted glass</li><li>Thermal &amp; acoustic glass</li></ul>
  <div class="abs" style="left:460px;top:26px"><div class="footer-heading">Follow us on</div>
    <ul class="footer-list social"><li><span class="dot"></span>Friendwall</li><li><span class="dot"></span>Snapgrid</li><li><span class="dot"></span>Pinboardly</li></ul></div>
  <div class="footer-heading abs" style="left:556px;top:26px">Sign-up to the Newsletter</div>
</footer>
<div class="newsletter abs"><span>Email Address</span>
  <svg width="11" height="8" viewBox="0 0 11 8"><rect width="11" height="8" fill="#333"/><path d="M0 0l5.5 4.5L11 0" stroke="#fff" fill="none" stroke-width="1"/></svg></div>
<div class="footer-rule abs"></div>
<p class="copyright abs">Copyright &copy; 2018 Clearvane glass &amp; hardwares. &nbsp; All rights reserved.</p>
</body>
</html>
```